Meridian Rest Supply Needs Business Card

Looking for a very nice looking business card. Creative but not extravagant. We sell beds and pillows across the U.S. and need something professional but catchy. I have attached the logo.

Name : Dale Fenwick
Title : President
Phone : (800) 417-2964
Email: sleep@quorvana.com
Website: www.quorvana.com

Can be single-sided or double-sided
horizontal or vertical

Can use Blues/Greys

Target Market(s)

Mass Market

Industry/Entity Type

Retail

Contact Information for Business Card

Name : Dale Fenwick
Title : President
Phone : (800) 417-2964
Email: sleep@quorvana.com
Website: www.quorvana.com

Requirements
Must have
• Clean, Modern, Smooth
• Can use Blues/Greys
• On the other side without the information - have something simple like www.quorvana.com or our logo
Nice to have
• Surprise me
Should not have
• Nothing crazy, nothing cluttered

```html
<!DOCTYPE html>
<html lang="en">
<head>
<meta charset="utf-8">
<title>Quorvana Business Card</title>
<link rel="stylesheet" href="https://fonts.googleapis.com/css2?family=Lato:wght@300;400;700;900&display=swap">
<style>
  :root {
    --backdrop: #5a5a5a;
    --brand-blue: #2f9bd1;
    --card-white: #f7f7f5;
    --ink-grey: #7a7a7a;
    --line-soft: rgba(255, 255, 255, 0.55);
    --text-white: #ffffff;
  }
  * { box-sizing: border-box; margin: 0; padding: 0; }
  html, body {
    width: 1200px;
    height: 725px;
    overflow: hidden;
    background: var(--backdrop);
    font-family: "Lato", sans-serif;
  }
  .stage {
    position: relative;
    width: 1200px;
    height: 725px;
    display: flex;
    align-items: center;
    justify-content: center;
    gap: 60px;
  }
  .card {
    position: relative;
    width: 500px;
    height: 286px;
    overflow: hidden;
  }
  /* Front: logo side */
  .card-front {
    background: var(--brand-blue);
    display: flex;
    align-items: center;
    justify-content: center;
  }
  .brand-name {
    font-family: "Lato", sans-serif;
    font-weight: 300;
    font-size: 92px;
    letter-spacing: 1px;
    color: var(--text-white);
    line-height: 1;
  }
  /* Back: contact side */
  .card-back {
    background: var(--card-white);
  }
  .identity {
    position: absolute;
    top: 62px;
    left: 0;
    width: 100%;
    text-align: center;
  }
  .person-name {
    font-weight: 900;
    font-size: 19px;
    letter-spacing: 0.5px;
    color: var(--brand-blue);
    text-transform: uppercase;
  }
  .person-title {
    margin-top: 1px;
    font-weight: 400;
    font-size: 10px;
    letter-spacing: 1.5px;
    color: var(--ink-grey);
    text-transform: uppercase;
  }
  .contact-band {
    position: absolute;
    top: 118px;
    left: 0;
    width: 100%;
    height: 140px;
    background: var(--brand-blue);
    display: flex;
    justify-content: space-around;
    align-items: flex-start;
    padding: 20px 30px 0;
  }
  .contact-item {
    width: 130px;
    display: flex;
    flex-direction: column;
    align-items: center;
  }
  .icon-ring {
    width: 64px;
    height: 64px;
    border: 1.5px dashed var(--line-soft);
    border-radius: 50%;
    display: flex;
    align-items: center;
    justify-content: center;
  }
  .icon-ring svg {
    width: 24px;
    height: 24px;
  }
  .contact-text {
    margin-top: 14px;
    font-size: 11px;
    font-weight: 400;
    color: var(--text-white);
    letter-spacing: 0.3px;
  }
</style>
</head>
<body>
  <main class="stage">
    <section class="card card-front" aria-label="Card front">
      <span class="brand-name">quorvana</span>
    </section>

    <section class="card card-back" aria-label="Card back">
      <div class="identity">
        <p class="person-name">Dale Fenwick</p>
        <p class="person-title">President</p>
      </div>

      <div class="contact-band">
        <div class="contact-item">
          <div class="icon-ring">
            <svg viewBox="0 0 24 24" aria-hidden="true">
              <path d="M3 9c0-2.5 4-4.5 9-4.5s9 2 9 4.5v1.5h-4.5V8.5c-1.3-.5-2.8-.7-4.5-.7s-3.2.2-4.5.7v2H3z" fill="#fff"/>
              <path d="M7 11h10l2.5 8H4.5z" fill="#fff"/>
              <circle cx="12" cy="15" r="2" fill="#2f9bd1"/>
            </svg>
          </div>
          <span class="contact-text">(800) 417-2964</span>
        </div>

        <div class="contact-item">
          <div class="icon-ring">
            <svg viewBox="0 0 24 24" aria-hidden="true">
              <rect x="3" y="6" width="18" height="12" fill="none" stroke="#fff" stroke-width="1.6"/>
              <path d="M3 6l9 7 9-7M3 18l7-6M21 18l-7-6" fill="none" stroke="#fff" stroke-width="1.4"/>
            </svg>
          </div>
          <span class="contact-text">sleep@quorvana.com</span>
        </div>

        <div class="contact-item">
          <div class="icon-ring">
            <svg viewBox="0 0 24 24" aria-hidden="true">
              <g fill="none" stroke="#fff" stroke-width="1.5">
                <circle cx="12" cy="12" r="9"/>
                <ellipse cx="12" cy="12" rx="4" ry="9"/>
                <path d="M3 12h18M4.5 7.5h15M4.5 16.5h15"/>
              </g>
            </svg>
          </div>
          <span class="contact-text">www.quorvana.com</span>
        </div>
      </div>
    </section>
  </main>
</body>
</html>
```